OpenCart Version 2.3.0.2 redesign for Retail and wholesale off road vehicles parts & accessor...

OpenCart Version 2.3.0.2 and want to upgrade to latest version if it is possible, and redesign for Retail and wholesale off road vehicles parts & accessories we are looking for a fresh new lookwe want it easy to usewe need it to be the same with 2 language Arabic/Englishwill work with both PC/mobileFixing the issues with all the current designWe have a logo we want to keep but its OK if slightly change it to work with the storeOur current website is: http://www.duneridgeparts.com

Target Market(s)

Cars parts

Industry/Entity Type

Automotive

```html
<!DOCTYPE html>
<html lang="en">
<head>
<meta charset="utf-8">
<title>Dune Ridge Parts — Off Road Parts &amp; Accessories</title>
<link href="https://fonts.googleapis.com/css2?family=Ubuntu:wght@300;400;500;700&family=Open+Sans:wght@400;600;700&display=swap" rel="stylesheet">
<style>
:root{
  --gold:#e6a817;
  --gold-dark:#cf950f;
  --ink:#2b2b2b;
  --panel:#2e2e2e;
  --grey-bg:#f4f4f4;
  --line:#e3b54a;
  --white:#ffffff;
}
*{box-sizing:border-box;margin:0;padding:0}
html,body{width:1200px;height:4500px;overflow:hidden}
body{font-family:"Open Sans",Arial,sans-serif;color:var(--ink);background:var(--white);position:relative}

/* top bar */
.topbar{height:30px;background:var(--gold);display:flex;align-items:center;padding:0 150px;color:var(--white);font-size:13px}
.topbar a{margin-right:36px;color:inherit;text-decoration:none}
.topbar .search{margin-left:auto;display:flex}
.topbar .search span{width:120px;height:16px;background:var(--white);border:1px solid #ddd}
.topbar .search b{width:40px;height:16px;background:#f7f7f7;margin-left:6px;border:1px solid #ddd}

/* header */
.header{height:75px;display:flex;align-items:center;padding:0 150px;border-bottom:1px solid #eee}
.brand{display:flex;align-items:center;gap:8px;font-family:"Ubuntu",sans-serif;font-weight:500;font-size:18px;color:var(--gold-dark)}
.brand i{width:20px;height:20px;background:var(--gold-dark);display:block}
.nav{margin-left:auto;display:flex;gap:22px;font-size:15px;color:var(--gold-dark)}
.nav .active{text-decoration:underline;font-weight:600}

/* hero */
.hero{height:385px;position:relative;background:linear-gradient(100deg,#3a3a3a 0%,#1c1c1c 40%,#5a5a5a 75%,#2a2a2a 100%);display:flex;flex-direction:column;align-items:center;justify-content:center;color:var(--white)}
.hero h1{font-family:"Ubuntu",sans-serif;font-weight:300;font-size:46px;letter-spacing:1px;line-height:1}
.hero h2{font-family:"Ubuntu",sans-serif;font-weight:700;font-size:38px;margin-top:6px;margin-left:120px;line-height:1}
.hero .arrow{position:absolute;top:172px}
.hero .prev{left:150px}.hero .next{right:150px}

/* section title */
.title{display:flex;align-items:center;justify-content:center;font-family:"Ubuntu",sans-serif;font-weight:700;font-size:36px;letter-spacing:3px;color:var(--ink)}
.title::before,.title::after{content:"";flex:1;height:1px;background:var(--line)}
.title span{padding:0 40px}
.title.grey::before,.title.grey::after{background:#ccc}

/* filter */
.filter{height:325px;padding-top:50px}
.filter .fields{display:flex;justify-content:space-between;padding:0 150px;margin-top:35px}
.field{width:232px;text-align:center}
.field label{font-size:15px;color:#777;font-weight:600}
.select{margin-top:10px;height:34px;display:flex;border:1px solid #ccc}
.select span{flex:1;text-align:left;padding:6px 10px;font-size:13px;color:#aaa}
.select b{width:48px;background:#a8a8a8;display:flex;align-items:center;justify-content:center}
.btn{background:var(--gold);color:var(--white);font-weight:700;font-size:15px;letter-spacing:2px;text-align:center}
.filter .btn{width:320px;height:38px;line-height:38px;margin:45px auto 0}

/* services */
.services{height:460px;background:linear-gradient(90deg,#151515,#2c2c2c 50%,#161616);color:var(--white);padding-top:70px}
.services .title{color:var(--white)}
.services .title::before,.services .title::after{display:none}
.service{display:flex;align-items:flex-start;gap:42px;padding:0 150px;margin-top:40px}
.service.right{flex-direction:row-reverse;text-align:right;margin-top:10px}
.service .icon{width:90px;height:90px;display:flex;align-items:center;justify-content:center;flex:none}
.service .icon.dark{background:#4a4a4a}
.service .icon.gold{background:var(--gold);margin-top:10px}
.service h3{font-family:"Ubuntu",sans-serif;font-weight:400;font-size:36px;line-height:1.1}
.service p{font-size:13px;line-height:1.45;width:520px;margin-top:10px}

/* products */
.products{background:var(--grey-bg)}
.featured{height:725px;padding-top:60px}
.latest{height:1200px;padding-top:60px}
.grid{display:flex;gap:36px;padding:0 150px;margin-top:85px}
.grid + .grid{margin-top:70px}
.card{width:198px;height:390px;background:var(--panel);position:relative;overflow:hidden}
.card .photo{height:195px;background:radial-gradient(circle at 50% 50%,#8a8a8a 0%,#d9d9d9 45%,#ffffff 70%)}
.card .photo.red{background:radial-gradient(circle at 50% 50%,#7a2020 0%,#bbbbbb 40%,#ffffff 70%)}
.card .photo.blue{background:radial-gradient(circle at 50% 50%,#2a3d8f 0%,#c6c6d6 45%,#ffffff 70%)}
.card .photo.black{background:radial-gradient(circle at 50% 50%,#2a2a2a 0%,#9a9a9a 40%,#ffffff 68%)}
.ribbon{position:absolute;top:18px;left:-30px;width:120px;height:26px;background:var(--gold);transform:rotate(-45deg);color:var(--white);font-size:13px;font-weight:700;text-align:center;line-height:26px;letter-spacing:1px}
.card .info{padding:10px 12px 0;color:var(--white)}
.price{font-size:25px;font-weight:700;font-family:"Ubuntu",sans-serif;white-space:nowrap}
.price s{color:#bbb;font-weight:400;font-size:22px;margin-left:6px}
.stars{font-size:20px;color:var(--gold);letter-spacing:2px;margin-top:2px}
.stars em{font-style:normal;color:var(--white)}
.card p{font-size:8.5px;line-height:1.35;color:#ddd;margin-top:8px;height:46px}
.card .add{display:block;height:20px;line-height:20px;margin-top:10px;background:var(--gold);font-size:9px;font-weight:700;text-align:center;letter-spacing:1px}
.card .add.off{background:#a8a8a8}
.more{width:238px;height:48px;line-height:48px;border-radius:24px;margin:55px auto 0;font-size:19px}

/* location */
.location{height:180px;padding-top:70px}
.map{height:360px;background:linear-gradient(135deg,#ecebe6 0%,#e4e2da 50%,#eeede8 100%)}

/* newsletter */
.newsletter{height:325px;background:var(--grey-bg);padding-top:40px}
.newsletter .title{background:var(--white);padding:15px 0}
.newsletter .input{width:900px;height:46px;margin:60px auto 0;background:var(--white);text-align:center;font-size:14px;color:#ccc;line-height:46px}
.newsletter .btn{width:282px;height:44px;line-height:44px;margin:25px auto 0;font-size:14px;font-weight:600;letter-spacing:1px}

/* footer */
.footer{height:435px;background:linear-gradient(90deg,#141414,#262626 50%,#141414);color:var(--white);padding:30px 150px 0}
.cols{display:flex}
.col{font-size:13px}
.col:nth-child(1){width:245px}.col:nth-child(2){width:282px}.col:nth-child(3){width:262px}
.col h4{font-size:15px;font-weight:700;letter-spacing:.5px;margin-bottom:50px}
.col li{list-style:none;line-height:30px;white-space:nowrap}
.social{text-align:center;margin-top:35px}
.social h5{font-size:15px;font-weight:700;text-decoration:underline;letter-spacing:.5px}
.social .dots{display:flex;justify-content:center;gap:21px;margin-top:18px}
.social .dots i{width:34px;height:34px;border-radius:50%;background:var(--white);display:block}
.copy{text-align:center;font-size:10px;margin-top:42px;color:#ddd}
</style>
</head>
<body>

<div class="topbar">
  <a>Register</a><a>Log In</a><a>My account</a>
  <div class="search"><span></span><b></b></div>
</div>

<header class="header">
  <div class="brand"><i></i>Dune Ridge Parts</div>
  <nav class="nav">
    <span class="active">Home</span><span>About US</span><span>Products</span><span>Brands</span><span>Contact US</span>
  </nav>
</header>

<section class="hero" role="img" aria-label="Dark photo of a car headlight and wheel">
  <svg class="arrow prev" width="24" height="40" viewBox="0 0 24 40"><path d="M20 4 L6 20 L20 36" stroke="#fff" stroke-width="6" fill="none"/></svg>
  <h1>WE CARE ABOUT</h1>
  <h2>YOUR CAR</h2>
  <svg class="arrow next" width="24" height="40" viewBox="0 0 24 40"><path d="M4 4 L18 20 L4 36" stroke="#fff" stroke-width="6" fill="none"/></svg>
</section>

<section class="filter">
  <h2 class="title grey"><span>Filter</span></h2>
  <div class="fields">
    <div class="field"><label>Make:</label><div class="select"><span>Select</span><b><svg width="18" height="12"><path d="M0 0 H18 L9 12Z" fill="#fff"/></svg></b></div></div>
    <div class="field"><label>Model:</label><div class="select"><span>Select</span><b><svg width="18" height="12"><path d="M0 0 H18 L9 12Z" fill="#fff"/></svg></b></div></div>
    <div class="field"><label>Year:</label><div class="select"><span>Select</span><b><svg width="18" height="12"><path d="M0 0 H18 L9 12Z" fill="#fff"/></svg></b></div></div>
  </div>
  <div class="btn">SUBMIT</div>
</section>

<section class="services">
  <h2 class="title"><span>OUR SERVISES</span></h2>
  <div class="service">
    <div class="icon dark"><svg width="50" height="50" viewBox="0 0 50 50"><circle cx="25" cy="25" r="20" fill="none" stroke="#fff" stroke-width="4"/><path d="M25 13 V25 H33" stroke="#fff" stroke-width="4" fill="none"/><text x="25" y="43" font-size="9" fill="#fff" text-anchor="middle" font-family="Open Sans, sans-serif">24h</text></svg></div>
    <div class="text">
      <h3>Lorem Ipsum Dolorsit</h3>
      <p>Lorem Ipsum is simply dummy text of the printing and typesetting industry. Lorem Ipsum has been the industry's standard dummy text ever since the 1500s, when an unknown printer took a galley of type and scrambled it to make a type specimen</p>
    </div>
  </div>
  <div class="service right">
    <div class="icon gold"><svg width="44" height="44" viewBox="0 0 44 44"><circle cx="22" cy="22" r="14" fill="none" stroke="#fff" stroke-width="6" stroke-dasharray="6 4"/><circle cx="22" cy="22" r="6" fill="#fff"/></svg></div>
    <div class="text">
      <h3>Lorem Ipsum Dolorsit</h3>
      <p>Lorem Ipsum is simply dummy text of the printing and typesetting industry. Lorem Ipsum has been the industry's standard dummy text ever since the 1500s, when an unknown printer took a galley of type and scrambled it to make a type specimen</p>
    </div>
  </div>
</section>

<div class="products">
<section class="featured">
  <h2 class="title"><span>FEATURED</span></h2>
  <div class="grid">
    <div class="card"><div class="photo red" role="img" aria-label="Tube of assembly lubricant"></div><div class="ribbon">NEW</div><div class="info"><div class="price">$14.99<s>$24.99</s></div><div class="stars">★★★<em>★★</em></div><p>Quality part built for off road use. Fits most models and ships fast from our local warehouse.</p><span class="add">ADD TO CART</span></div></div>
    <div class="card"><div class="photo red" role="img" aria-label="Black valve part with red fitting"></div><div class="info"><div class="price">$14.99<s>$24.99</s></div><div class="stars">★★★<em>★★</em></div><p>Quality part built for off road use. Fits most models and ships fast from our local warehouse.</p><span class="add off">ADD TO CART</span></div></div>
    <div class="card"><div class="photo black" role="img" aria-label="Bottle of engine oil"></div><div class="info"><div class="price">$14.99<s>$24.99</s></div><div class="stars">★★★<em>★★</em></div><p>Quality part built for off road use. Fits most models and ships fast from our local warehouse.</p><span class="add">ADD TO CART</span></div></div>
    <div class="card"><div class="photo" role="img" aria-label="Wheel spacer with bolts"></div><div class="ribbon">NEW</div><div class="info"><div class="price">$14.99<s>$24.99</s></div><div class="stars">★★★<em>★★</em></div><p>Quality part built for off road use. Fits most models and ships fast from our local warehouse.</p><span class="add">ADD TO CART</span></div></div>
  </div>
  <div class="btn more">SHOW MORE ▼</div>
</section>

<section class="latest">
  <h2 class="title"><span>LATEST</span></h2>
  <div class="grid">
    <div class="card"><div class="photo black" role="img" aria-label="Pair of suspension control arms"></div><div class="info"><div class="price">$14.99<s>$24.99</s></div><div class="stars">★★★<em>★★</em></div><p>Quality part built for off road use. Fits most models and ships fast from our local warehouse.</p><span class="add">ADD TO CART</span></div></div>
    <div class="card"><div class="photo black" role="img" aria-label="Coil spring spacers"></div><div class="ribbon">NEW</div><div class="info"><div class="price">$14.99<s>$24.99</s></div><div class="stars">★★★<em>★★</em></div><p>Quality part built for off road use. Fits most models and ships fast from our local warehouse.</p><span class="add">ADD TO CART</span></div></div>
    <div class="card"><div class="photo blue" role="img" aria-label="Polyurethane bushing kit"></div><div class="ribbon">NEW</div><div class="info"><div class="price">$14.99<s>$24.99</s></div><div class="stars">★★★<em>★★</em></div><p>Quality part built for off road use. Fits most models and ships fast from our local warehouse.</p><span class="add">ADD TO CART</span></div></div>
    <div class="card"><div class="photo black" role="img" aria-label="Rubber spring seat"></div><div class="info"><div class="price">$14.99<s>$24.99</s></div><div class="stars">★★★<em>★★</em></div><p>Quality part built for off road use. Fits most models and ships fast from our local warehouse.</p><span class="add off">ADD TO CART</span></div></div>
  </div>
  <div class="grid">
    <div class="card"><div class="photo black" role="img" aria-label="Pair of suspension control arms"></div><div class="ribbon">NEW</div><div class="info"><div class="price">$14.99<s>$24.99</s></div><div class="stars">★★★<em>★★</em></div><p>Quality part built for off road use. Fits most models and ships fast from our local warehouse.</p><span class="add off">ADD TO CART</span></div></div>
    <div class="card"><div class="photo black" role="img" aria-label="Coil spring spacers"></div><div class="info"><div class="price">$14.99<s>$24.99</s></div><div class="stars">★★★<em>★★</em></div><p>Quality part built for off road use. Fits most models and ships fast from our local warehouse.</p><span class="add">ADD TO CART</span></div></div>
    <div class="card"><div class="photo blue" role="img" aria-label="Polyurethane bushing kit"></div><div class="info"><div class="price">$14.99<s>$24.99</s></div><div class="stars">★★★<em>★★</em></div><p>Quality part built for off road use. Fits most models and ships fast from our local warehouse.</p><span class="add">ADD TO CART</span></div></div>
    <div class="card"><div class="photo black" role="img" aria-label="Rubber spring seat"></div><div class="ribbon">NEW</div><div class="info"><div class="price">$14.99<s>$24.99</s></div><div class="stars">★★★<em>★★</em></div><p>Quality part built for off road use. Fits most models and ships fast from our local warehouse.</p><span class="add">ADD TO CART</span></div></div>
  </div>
  <div class="btn more">SHOW MORE ▼</div>
</section>
</div>

<section class="location">
  <h2 class="title"><span>LOCATION</span></h2>
</section>
<div class="map" role="img" aria-label="Street map showing the store location"></div>

<section class="newsletter">
  <h2 class="title"><span>NEWSLETTER</span></h2>
  <div class="input">Your E-mail Address Here</div>
  <div class="btn">SUBCRIBE</div>
</section>

<footer class="footer">
  <div class="cols">
    <div class="col"><h4>OPENNING TIME</h4><ul><li>Saturday - Thursday</li><li>From &nbsp;&nbsp;&nbsp;08:00 am</li><li>To &nbsp;&nbsp;&nbsp;&nbsp;&nbsp;&nbsp;&nbsp;07:00 pm</li><li>E-Mail: sales@duneridgeparts.com</li><li>WhatsApp: 00966500012345</li></ul></div>
    <div class="col"><h4>CUSTOMER SERVICE</h4><ul><li>Contact Us</li><li>Returns</li><li>Site Map</li><li>Brands</li><li>Gift Certificates</li></ul></div>
    <div class="col"><h4>INFORMATION</h4><ul><li>Installition Service</li><li>About Us</li><li>Delivery Information</li><li>Privacy Policy</li><li>Terms &amp; Conditions</li></ul></div>
    <div class="col"><h4>MY ACCOUNT</h4><ul><li>My Account</li><li>Order History</li><li>Wish List</li><li>Newsletter</li><li>Specials</li></ul></div>
  </div>
  <div class="social">
    <h5>FOLLOW US ON SOCIAL MEDIA</h5>
    <div class="dots"><i></i><i></i><i></i><i></i><i></i></div>
  </div>
  <p class="copy">Copyright © 2016 Web Design. All source reserved.</p>
</footer>

</body>
</html>
```